Business Card Design

We need a sharp, bold, crisp logo and business card that helps express confidence in what we do. The logo can either have the name of the company in it, or somehow use the first initials of each of the two words in the name, or it doesn't have to have any text in the logo at all.

Target Market(s)

Upper management of small to midsize companies (Presidents, CEOs, Executive Directors, Executive Managers, etc.)

Industry/Entity Type

Business

Contact Information for Business Card

Name of company: Brightpath Advisors, LLC;
My name and title: Dana Melkovic - President;
My phone number: 555-318-2070;
My email address: dana@brightpathadvisors.example;
The website: www.brightpathadvisors.example

Requirements
Must have
• Bullets of what we do: - Quality Systems Development & Implementation, - Process Improvement Services, - Problem Solving Services, - Quality System Auditing, - Customized In-House Training, - TeamVault Site Development
Nice to have
• What we do: We specialize in Quality Systems & Process Improvement Consulting Services. We help non-automotive industries and automotive suppliers to achieve and exceed their Quality and Efficiency goals by leveraging and applying a tremendous amount of excellent automotive industry quality systems experience into your organization’s processes.

```html
<!DOCTYPE html>
<html lang="en">
<head>
<meta charset="utf-8">
<title>Brightpath Advisors, LLC – Business Card</title>
<link rel="stylesheet" href="https://fonts.googleapis.com/css2?family=Cinzel:wght@400&family=Questrial&display=swap">
<style>
  :root {
    --page: #ffffff;
    --ink: #000000;
    --card-black: #050505;
    --gold-light: #f4f28e;
    --gold-mid: #e6e06a;
    --gold-deep: #c7b930;
    --strip-light: #f3f1a8;
    --strip-deep: #ddd373;
    --pale-text: #f3efa0;
    --white-text: #f4f2d6;
    --icon-red: #d9341f;
  }
  * { box-sizing: border-box; margin: 0; padding: 0; }
  html, body {
    width: 985px; height: 1200px; overflow: hidden;
    background: var(--page);
  }
  .canvas { position: relative; width: 985px; height: 1200px; }

  .card { position: absolute; left: 27px; width: 932px; overflow: hidden; background: var(--card-black); }
  .card-front { top: 28px; height: 545px; }
  .card-back { top: 628px; height: 544px; }

  .card-shape { position: absolute; inset: 0; width: 100%; height: 100%; }

  .company-name {
    position: absolute; top: 96px; left: 0; width: 100%;
    text-align: center;
    font-family: "Cinzel", serif; font-weight: 400; font-size: 31px; letter-spacing: 1.5px;
    text-transform: uppercase;
    color: var(--pale-text);
  }
  .person { position: absolute; top: 293px; left: 0; width: 100%; text-align: center; color: var(--ink); font-family: "Questrial", sans-serif; }
  .person-name { font-size: 36px; line-height: 44px; }
  .person-title { font-size: 20px; line-height: 26px; }

  .contact-line {
    position: absolute; top: 430px; left: 0; width: 100%;
    display: flex; justify-content: center; align-items: center; gap: 12px;
    font-family: "Questrial", sans-serif; font-size: 19.5px; color: var(--ink);
  }
  .contact-item { display: flex; align-items: center; gap: 8px; white-space: nowrap; }
  .contact-icon { width: 26px; height: 26px; flex: none; }

  .services-heading {
    position: absolute; top: 156px; left: 80px; width: 300px; text-align: center;
    font-family: "Questrial", sans-serif; font-weight: 400; font-size: 28.5px; letter-spacing: 0.5px;
    color: var(--pale-text);
  }
  .services-list {
    position: absolute; top: 209px; left: 52px; list-style: none;
    font-family: "Questrial", sans-serif; font-size: 23px; line-height: 28.6px;
    color: var(--white-text); white-space: nowrap;
  }
  .services-list li { position: relative; padding-left: 27px; }
  .services-list li::before {
    content: ""; position: absolute; left: 0; top: 8px;
    width: 13px; height: 13px; border-radius: 50%; background: var(--gold-light);
  }
  .divider { position: absolute; left: 455px; top: 112px; width: 2px; height: 305px; background: var(--pale-text); }
  .about {
    position: absolute; top: 120px; left: 512px; width: 410px;
    font-family: "Questrial", sans-serif; font-size: 23px; line-height: 28.6px;
    color: var(--pale-text); white-space: nowrap;
  }
  .about .lead-letter { font-size: 38px; line-height: 20px; }
</style>
</head>
<body>
<div class="canvas">

  <section class="card card-front" aria-label="Business card front">
    <svg class="card-shape" viewBox="0 0 932 545" preserveAspectRatio="none" aria-hidden="true">
      <defs>
        <radialGradient id="goldGlow" cx="0.5" cy="0.55" r="0.65">
          <stop offset="0" stop-color="var(--gold-light)"/>
          <stop offset="0.55" stop-color="var(--gold-mid)"/>
          <stop offset="1" stop-color="var(--gold-deep)"/>
        </radialGradient>
        <linearGradient id="stripGlow" x1="0" x2="1" y1="0" y2="0">
          <stop offset="0" stop-color="var(--strip-deep)"/>
          <stop offset="0.5" stop-color="var(--strip-light)"/>
          <stop offset="1" stop-color="var(--strip-deep)"/>
        </linearGradient>
      </defs>
      <path d="M0 277 Q475 134 932 287 L932 545 L0 545 Z" fill="url(#goldGlow)"/>
      <rect x="0" y="509" width="932" height="36" fill="url(#stripGlow)"/>
    </svg>

    <h1 class="company-name">Brightpath Advisors, LLC</h1>

    <div class="person">
      <p class="person-name">Dana Melkovic</p>
      <p class="person-title">President</p>
    </div>

    <div class="contact-line">
      <span class="contact-item">
        <svg class="contact-icon" viewBox="0 0 26 26" aria-hidden="true">
          <circle cx="13" cy="13" r="11.5" fill="none" stroke="var(--icon-red)" stroke-width="2"/>
          <path d="M9 7.5 L11 7.5 L12 10.5 L10.6 11.6 Q12 14.5 14.4 15.4 L15.5 14 L18.5 15 L18.5 17 Q17.5 18.6 15.5 18.3 Q9.5 17 7.8 10.5 Q7.6 8.4 9 7.5 Z" fill="var(--icon-red)"/>
        </svg>
        555-318-2070
      </span>
      <span class="contact-item">
        <svg class="contact-icon" viewBox="0 0 26 26" aria-hidden="true">
          <circle cx="13" cy="13" r="11.5" fill="none" stroke="var(--icon-red)" stroke-width="2"/>
          <text x="13" y="17.5" text-anchor="middle" font-family="Arial, sans-serif" font-size="14" fill="var(--icon-red)">@</text>
        </svg>
        dana@brightpathadvisors.example
      </span>
      <span class="contact-item">
        <svg class="contact-icon" viewBox="0 0 26 26" aria-hidden="true">
          <g fill="none" stroke="var(--icon-red)" stroke-width="1.8">
            <circle cx="13" cy="13" r="11.5"/>
            <ellipse cx="13" cy="13" rx="5" ry="11.5"/>
            <line x1="1.5" y1="13" x2="24.5" y2="13"/>
            <path d="M3.5 7.5 H22.5 M3.5 18.5 H22.5"/>
          </g>
        </svg>
        www.brightpathadvisors.example
      </span>
    </div>
  </section>

  <section class="card card-back" aria-label="Business card back">
    <svg class="card-shape" viewBox="0 0 932 544" preserveAspectRatio="none" aria-hidden="true">
      <defs>
        <linearGradient id="backStrip" x1="0" x2="1" y1="0" y2="0">
          <stop offset="0" stop-color="var(--strip-deep)"/>
          <stop offset="0.5" stop-color="var(--strip-light)"/>
          <stop offset="1" stop-color="var(--strip-deep)"/>
        </linearGradient>
      </defs>
      <rect x="0" y="493" width="932" height="15" fill="var(--gold-deep)"/>
      <rect x="0" y="508" width="932" height="36" fill="url(#backStrip)"/>
    </svg>

    <h2 class="services-heading">-WHAT WE DO -</h2>
    <ul class="services-list">
      <li>Quality Systems Development &amp;<br>Implementation,</li>
      <li>Process Improvement Services,</li>
      <li>Problem Solving Services,</li>
      <li>Quality System Auditing,</li>
      <li>Customized In-House Training,</li>
      <li>TeamVault Site Development</li>
    </ul>

    <div class="divider"></div>

    <p class="about"><span class="lead-letter">W</span>e specialize in Quality Systems &amp;<br>Process Improvement Consulting<br>Services. We help non-automotive<br>industries and automotive suppliers<br>to achieve and exceed their Quality<br>and Efficiency goals by leveraging<br>and applying a tremendous amount<br>of excellent automotive industry<br>quality systems experience into<br>your organization’s processes.</p>
  </section>

</div>
</body>
</html>
```